New Payments Start-up requires Logo, Style Guide and Web Site Design

We need a logo, style guide (colour templates etc.) and marketing web-site (HTML/CSS styling) for Brixu, a new account-to-account payment product for use in the Single European Payment Area (SEPA).

The design is for the product only, not a company brand. We're looking for basic palette and style guidelines also. The web site need only be a basic responsive cross-platform design and layout. We will produce our own content.

We have no requirements for specific colours or logo styles. It is a financial product, however, so should not appear too quirky or untrustworthy.

The product is still in the early phases of development, so we're not able to provide pictures or other content.

As a little more detail on how things work, though, our end customers will arrive at our site through redirection from our merchant partners (a number of whom are large multi-national companies) who have offered our services as an alternative to credit card payments. They will be able to set up a SEPA direct debit mandate online in just a few pages, secure that with a password and use it to pay both immediately and in future with a simple confirmation of the password… a quick, easy checkout.

Because we work with large customer in the payments space, whilst we’d like the brand to be modern and appealing, it has to engender trust and stability. Whilst this product is new and in start-up phase, our company has been in alternative payments for nearly 10 years and have strong products in Europe in the Pre-Paid Zent/KelvaPort and Voucher space. We'd like to treat this separately, however, which is why we've briefed accordingly.
Updates

Reason: Apologies for the extension, but I had a couple of designers contact me to say they had completed work but were unable to submit because time ran out. I'll only extend this once, though, because we need to get cracking on the project. Many thanks Tev

Target Market(s)

European alternative payment customers

Industry/Entity Type

Financial

Logo Text

brixu

Coding

Coded - Design and coding required

Number of Pages Required

1 page

Font styles to use
Sans Serif

```html
<!DOCTYPE html>
<html lang="en">
<head>
<meta charset="utf-8">
<title>Brixu</title>
<link rel="stylesheet" href="https://fonts.googleapis.com/css2?family=Open+Sans:wght@400;600;700;800&family=Roboto+Condensed:wght@700&display=swap">
<style>
  :root {
    --orange: #f7921e;
    --orange-deep: #f0690f;
    --orange-light: #fbab2c;
    --orange-pale: #fcc15a;
    --card: #f9a21c;
    --card-edge: #fdc25c;
    --white: #ffffff;
    --cream: #fff3e0;
    --grey-line: #c9c9c9;
    --link: #c7400a;
    --rss-grey: #777777;
  }
  * { margin: 0; padding: 0; box-sizing: border-box; }
  html, body { width: 1200px; height: 900px; overflow: hidden; background: var(--white); }
  body { position: relative; font-family: "Open Sans", Arial, sans-serif; }

  .page {
    position: absolute; left: 166px; top: 0; width: 900px; height: 900px; overflow: hidden;
    background: linear-gradient(180deg, var(--orange-light) 0%, var(--orange) 30%, var(--orange) 70%, var(--orange-deep) 100%);
  }
  .header-curve { position: absolute; left: 0; top: 0; width: 900px; height: 320px; }
  .top-link { position: absolute; left: 58px; top: 14px; font-size: 10px; color: var(--white); white-space: nowrap; }
  .top-link a { color: var(--white); font-weight: 700; text-decoration: underline; }
  .top-link .home-icon { display: inline-block; width: 8px; height: 8px; border: 1.5px solid var(--white); border-radius: 50%; margin-right: 8px; vertical-align: middle; }

  .wordmark { position: absolute; font-family: "Open Sans", Arial, sans-serif; font-weight: 800; letter-spacing: 4px; line-height: 1; white-space: nowrap; }
  .wordmark--header { left: 50px; top: 116px; font-size: 56px; color: var(--orange); }
  .wordmark--welcome { left: 578px; top: 382px; font-size: 56px; color: var(--white); }

  .hero-art {
    position: absolute; left: 374px; top: 26px; width: 526px; height: 262px;
    background: linear-gradient(100deg, #f5c23a 0%, #f2e6d6 38%, #f3b6c4 58%, #b9d8f0 78%, #d9efcf 100%);
    border-radius: 40px 0 0 60px;
  }
  .rss { position: absolute; left: 741px; top: 74px; font-size: 9px; color: var(--rss-grey); letter-spacing: 0.5px; display: flex; align-items: center; gap: 6px; white-space: nowrap; }

  .main-nav { position: absolute; left: 0; top: 320px; width: 900px; height: 36px; display: flex; }
  .main-nav a {
    font-family: "Roboto Condensed", Arial, sans-serif; font-size: 14px; color: var(--white); white-space: nowrap;
    text-decoration: none; line-height: 36px; padding: 0 16px 0 22px; border-right: 1px solid rgba(255,255,255,0.35);
    background: linear-gradient(180deg, rgba(255,255,255,0.18), rgba(255,255,255,0));
  }

  .product-box {
    position: absolute; left: 74px; top: 405px; width: 132px; height: 157px;
    background: linear-gradient(135deg, #f4f4f4 0%, #f2a030 45%, #c9650d 70%, #ececec 100%);
    border-radius: 4px; box-shadow: 0 6px 10px rgba(120,50,0,0.35);
  }
  .welcome-title { position: absolute; left: 236px; top: 416px; font-size: 22px; font-weight: 700; color: var(--white); white-space: nowrap; }
  .welcome-rule { position: absolute; left: 236px; top: 451px; width: 560px; height: 1px; background: rgba(255,255,255,0.45); }
  .welcome-lead { position: absolute; left: 242px; top: 461px; font-size: 13px; color: var(--white); font-weight: 600; }
  .welcome-text { position: absolute; left: 242px; top: 482px; width: 612px; font-size: 10.5px; line-height: 20px; color: var(--white); }

  .footer-band { position: absolute; left: 0; top: 780px; width: 900px; height: 120px; background: linear-gradient(180deg, var(--orange-deep), #ee5a0c); }

  .card {
    position: absolute; top: 615px; width: 246px; height: 222px; border-radius: 6px;
    background: linear-gradient(180deg, var(--card) 0%, #f89818 100%);
    border: 2px solid var(--card-edge); box-shadow: 0 2px 6px rgba(150,60,0,0.3);
  }
  .card--checkout { left: 64px; }
  .card--merchants { left: 336px; }
  .card--security { left: 606px; }
  .card-title { position: absolute; left: 16px; top: 12px; font-size: 21px; font-weight: 700; color: var(--white); display: flex; align-items: center; gap: 10px; white-space: nowrap; }
  .card-title .bullet { width: 14px; height: 14px; border-radius: 50%; border: 2px solid var(--white); background: var(--cream); }
  .card-photo {
    position: absolute; left: 20px; top: 66px; width: 206px; height: 68px; border-radius: 6px;
    background: linear-gradient(100deg, #8a8f9a 0%, #2f3238 55%, #d9c3b0 100%);
  }
  .card-text { position: absolute; left: 26px; color: var(--white); font-size: 10.5px; line-height: 17px; }
  .card-text strong { font-size: 13.5px; font-weight: 400; }
  .card--checkout .card-text { top: 155px; }
  .card--security .card-text { top: 62px; width: 200px; }
  .link-list { position: absolute; left: 24px; top: 62px; list-style: none; font-size: 9px; line-height: 18.5px; white-space: nowrap; }
  .link-list li::before { content: "\25AA"; color: var(--link); margin-right: 3px; }
  .link-list a { color: var(--link); text-decoration: underline; }
  .tools-icon {
    position: absolute; left: 156px; top: 64px; width: 58px; height: 58px; border-radius: 50%;
    background: radial-gradient(circle at 40% 35%, #fbd08a, #e3830f 70%);
  }
  .read-more {
    position: absolute; left: 26px; top: 188px; width: 80px; height: 20px; border-radius: 10px;
    background: var(--orange-deep); border: 1px solid var(--card-edge); color: var(--white);
    font-size: 9px; line-height: 18px; text-align: center; text-decoration: none; padding-left: 8px;
  }
  .read-more::before { content: ""; position: absolute; left: 6px; top: 5px; width: 8px; height: 8px; border-radius: 50%; background: var(--cream); }

  .footer-links { position: absolute; left: 92px; top: 864px; font-size: 10px; color: var(--white); }
  .footer-links a { color: var(--orange-pale); text-decoration: underline; }
  .copyright { position: absolute; left: 636px; top: 864px; font-size: 10px; color: var(--white); white-space: nowrap; }
</style>
</head>
<body>
<div class="page">
  <svg class="header-curve" viewBox="0 0 900 320" aria-hidden="true">
    <path d="M0 60 Q450 10 900 28 L900 255 Q450 320 0 262 Z" fill="#c9c9c9"/>
    <path d="M0 56 Q450 6 900 24 L900 248 Q450 312 0 256 Z" fill="#ffffff"/>
  </svg>

  <div class="top-link"><span class="home-icon"></span><a href="#">www.brixu-pay.eu</a> // home page</div>

  <div class="hero-art" role="img" aria-label="Colourful product image with swatches in warm and pastel tones"></div>

  <div class="rss">
    <svg width="14" height="14" viewBox="0 0 14 14" aria-hidden="true"><rect width="14" height="14" rx="2" fill="#999"/><circle cx="4" cy="10" r="1.5" fill="#fff"/><path d="M3 6a5 5 0 0 1 5 5M3 3a8 8 0 0 1 8 8" stroke="#fff" stroke-width="1.5" fill="none"/></svg>
    SUBSCRIBE TO RSS FEED
  </div>

  <div class="wordmark wordmark--header">BRIXU</div>

  <nav class="main-nav">
    <a href="#">HOME PAGE</a><a href="#">ABOUT US</a><a href="#">HOW IT WORKS</a><a href="#">SECURITY</a><a href="#">MERCHANTS</a><a href="#">CONTACTS</a>
  </nav>

  <div class="product-box" role="img" aria-label="Product package image"></div>
  <h1 class="welcome-title">Welcome to our web site</h1>
  <div class="wordmark wordmark--welcome">BRIXU</div>
  <div class="welcome-rule"></div>
  <p class="welcome-lead">Lorem ipsum dolor sit amet</p>
  <p class="welcome-text">Consectetur adi piscing elit. Mauris quis dolor ac ante dapibus rhoncus. Nam ut ligula. Maecenas ut mi varius magna faucibus aliquam. Vestibulum volutpat. Vestibulum mi enim, sagittis ac, male suada quis, viverra tristique, metus. Nam ali quam est sit amet erat mattis placerat. Ut lobortis. Morbi a ante tristique nulla semper consectetur. Nullam eget arcu id ligula.</p>

  <div class="footer-band"></div>

  <section class="card card--checkout">
    <h2 class="card-title"><span class="bullet"></span>Checkout</h2>
    <div class="card-photo" role="img" aria-label="Hands typing on a laptop keyboard"></div>
    <p class="card-text"><strong>Lorem ipsum dolor sit amet</strong><br>Consectetur adi piscing elit.</p>
  </section>

  <section class="card card--merchants">
    <h2 class="card-title"><span class="bullet"></span>Merchants</h2>
    <ul class="link-list">
      <li><a href="#">Direct debit mandate</a></li>
      <li><a href="#">Secure password</a></li>
      <li><a href="#">Quick checkout</a></li>
      <li><a href="#">Merchant partners</a></li>
      <li><a href="#">SEPA coverage area</a></li>
    </ul>
    <div class="tools-icon" role="img" aria-label="Round tools icon"></div>
    <a class="read-more" href="#">read more</a>
  </section>

  <section class="card card--security">
    <h2 class="card-title"><span class="bullet"></span>Security</h2>
    <p class="card-text"><strong>Lorem ipsum dolor sit amet</strong><br>Consectetur adi piscing elit. Mauris quis dolor ac ante dapibus rhoncus. Nam ut ligula. Maecenas ut mi varius magna faucibus aliquam. Vestibulum volutpat. Vestibulum mi enim.</p>
    <a class="read-more" href="#">read more</a>
  </section>

  <p class="footer-links"><a href="#">Terms of Use</a> | <a href="#">Privacy Statement</a></p>
  <p class="copyright">© 2009 Your Corporation. All rights reserved</p>
</div>
</body>
</html>
```